■レイアウトの希望について
◎全体の左右のサイズは、1000px~1100pxくらいでお願いします。
※左右のサイドにナビを入れる場合は、左右300pxでお願いします。
◎現在のレイアウトは無視してください。
◎重要箇所を目立たせて、全体的にバランスよく配置させてください。
※重要箇所の順位は以下の通りです。
(1)検索ページへの入り口ブロック
(2)記事ページへのナビゲーション
(3)「イチオシ学生会館紹介サイト」と「オススメ学生会館」
(4)「学生会館以外のお部屋探し」
(5)「TOPICS」と「オススメ情報」
※見本のPDFは左ナビがあるようにレイアウトしていますが、トップページは2カラムにせず、1カラムでもかまいません。
(トップページに入れたいブロックを記載しただけですのでレイアウトの希望ではありません)
ただし、サブページは左右どちらかにナビを置く形の2カラムでお願いします。
(サブページのナビに入れるのは、記事ページへのナビゲーションと「学生会館以外のお部屋探し」のみです)

■デザインの希望について
◎落ち着いた感じのバランスの良いデザイン案が希望です。
※色数を多く使ったごちゃごちゃした配置は好みではありません。
※色は派手な感じでなく落ち着いた色が希望ですが、くすんだ色は好みではありません。
◎以前にツクリバで依頼して作成した下記サイトもご参照ください。
http://www.heyanavi-k.net/
http://www.kq3.net/
http://www.fineyd.com/
http://247.qxo.jp/sumiru.net/
※一番下のみ現在作成中のため仮URLです。(全ページは完成していません)

■その他の希望について
◎ヘッダーはスマホサイズになった場合のことも考えて作成してください。
◎提案内で使用するイメージ画像は無料の素材サイトか、有料画像を使用する場合は、FOTROをご利用ください。
https://fotro.jp/
※現在サイト内にある画像を使用いただく形でもかまいません。

なお、初回のご提案はできるだけ締切日の2日前までにお願いします。
ギリギリの場合は修正依頼が間に合わず、候補になる良いご提案でも見送る場合がありますので..。

以上になりますので、ご提案のほど、よろしくお願いいたします。
http://www.manabiyanokura.net/
3ページ
基本的にはお任せですが、派手な色やくすんだ色は避けてください。(バランスの良い、落ち着いた色が希望)
• 高解像度JPG (.jpg)
• フォトショップ形式 (.psd)
JPG・PNGはどちらでもかまいません。
残り2日になりましたが、提案がないので締切日を延長いたします。

依頼詳細にも記載しましたが、できるだけ締切日の2日前までに初回のご提案をお送りいただけましたら幸いです。

その他、ご要望などがございましたら、メッセージからお送りください。
ロゴは現在のものは使用せず、見本と同様の一般的な横長のものを希望します。
(ロゴではなくて書体をそのまま使用する形でもかまいません)
弊社希望の「全体の左右のサイズは、1000px~1100pxくらい」とうのは、実際に文章や画像が入る本文(左右ナビが入る場合はその外側まで)のサイズになりますので、ご確認ください。

なお、すでにご提案を作成中の場合で、上記に当てはまらない場合はそのまま進めていただいてもかまいません。

とりあえず、デザインが分かれば問題ありませんので..。

※実際にお仕事を依頼することになった場合は、修正をお願いします。
お仕事が決まったあとに作成していただく、サブページのレイアウトを作成しましたので添付します。

決定したトップページと同じ方向性で、こちらのサブページも作成いただく形でお願いします。
今月末まで多忙になり、選考作業や細かい修正依頼作業がすぐにはできそうもないので、締切日をギリギリまで延ばさせていただきます。

必ず当選者は選定させていただきますので、よろしくお願いいたします。

また、依頼金額も若干アップさせていただきました。

全体的なバランスが良く、ごちゃごちゃしていなくて、統一感があり落ち着いた感じのご提案でした。

ご提案をいただき、ありがとうございました。
部分的には気に入ったご提案もあったのですが、全体的なバランスやメリハリといった点で、採用した案を選びました。
申し訳ございませんがご了承ください。
なお、今後も複数サイトのリニューアル依頼をツクリバに出しますので、機会がございましたら、よろしくお願いいたします。

```html
<!DOCTYPE html>
<html lang="ja">
<head>
<meta charset="utf-8">
<title>学生会館 STAY-NAVI</title>
<link rel="stylesheet" href="https://fonts.googleapis.com/css2?family=Noto+Sans+JP:wght@400;500;700&display=swap">
<style>
:root{
  --orange:#f0891e;
  --orange-dark:#d9700c;
  --orange-pale:#fdf0e2;
  --ink:#3a3a3a;
  --muted:#888;
  --line:#e4e0da;
  --bg:#ffffff;
  --band:#f5f2ee;
  --dark:#2f2f2f;
  --label-blue:#5aa0d6;
  --label-green:#7bb65a;
  --label-purple:#a27bc4;
}
*{box-sizing:border-box;margin:0;padding:0}
html,body{width:1200px;height:2464px;overflow:hidden}
body{font-family:"Noto Sans JP",sans-serif;color:var(--ink);background:var(--bg);font-size:13px}
.wrap{width:880px;margin:0 auto;position:relative}

.site-header{height:52px;border-bottom:3px solid var(--orange);background:#fff}
.site-header .wrap{width:1140px;display:flex;align-items:center;height:49px}
.brand{font-weight:700;font-size:20px;color:var(--orange);display:flex;align-items:center;gap:8px}
.brand small{font-size:13px;color:var(--ink)}
.global-nav{margin-left:auto;display:flex;gap:26px;font-size:12px;color:var(--ink)}
.entry-btn{margin-left:28px;background:var(--orange);color:#fff;font-weight:700;font-size:12px;padding:10px 22px}

.hero{height:378px;position:relative;background:linear-gradient(120deg,#e9dccb,#c9b9a5 45%,#e6ddd1);}
.hero-bg{position:absolute;inset:0}
.hero-copy{position:relative;width:560px;margin:0 auto;padding-top:40px;text-align:center}
.hero-copy h1{font-size:24px;font-weight:700;color:#333}
.hero-copy p{font-size:12px;line-height:1.8;margin-top:10px;color:#444}
.search-bar{position:relative;width:720px;margin:22px auto 0;background:var(--orange);padding:10px 12px}
.search-bar .tabs{font-size:11px;color:#fff;margin-bottom:6px}
.search-row{display:flex;gap:6px}
.search-row .select{width:140px;background:#fff;height:34px;font-size:12px;line-height:34px;padding-left:10px;font-weight:700}
.search-row .field{flex:1;background:#fff;height:34px;font-size:11px;color:var(--muted);line-height:34px;padding-left:10px}
.search-row .go{width:40px;height:34px;background:var(--orange-dark);display:flex;align-items:center;justify-content:center}
.quick{position:relative;display:flex;gap:14px;justify-content:center;margin-top:28px}
.quick a{display:flex;align-items:center;background:#fff;border:1px solid var(--line);height:42px;width:170px;text-decoration:none;color:var(--ink);font-size:12px;font-weight:700}
.quick a span.ic{width:42px;height:42px;background:var(--orange);margin-right:10px}
.quick a em{font-style:normal;color:var(--orange);font-size:15px}

.notice-line{height:40px;font-size:11px;text-align:center;line-height:40px;color:var(--muted)}

.sec-title{text-align:center;margin-bottom:26px}
.sec-title h2{font-size:20px;font-weight:700}
.sec-title span{display:block;font-size:10px;color:var(--orange);letter-spacing:.1em;margin-top:2px}
.sec-title::after{content:"";display:block;width:40px;height:2px;background:var(--orange);margin:8px auto 0}

.about{height:520px;padding-top:30px}
.about-main{display:flex;gap:20px;margin-bottom:20px}
.about-main a{flex:1;height:92px;background:var(--orange);color:#fff;display:flex;align-items:center;text-decoration:none;padding:0 22px;gap:18px}
.about-main .icon{width:56px;height:56px;border-radius:6px;background:#fff}
.about-main b{font-size:17px;display:block}
.about-main small{font-size:11px}
.about-grid{display:grid;grid-template-columns:repeat(3,1fr);gap:16px}
.about-grid a{height:96px;border:1px solid var(--line);background:var(--orange-pale);display:flex;align-items:center;padding:0 16px;gap:14px;text-decoration:none;color:var(--ink)}
.about-grid .icon{width:52px;height:52px;border-radius:6px;background:var(--orange);flex:none}
.about-grid b{font-size:14px;display:block}
.about-grid small{font-size:10px;color:var(--muted)}

.recommend{height:390px;background:linear-gradient(90deg,#e8e1d8,#f3efe9 50%,#ddd4c8);padding-top:30px}
.cards{display:flex;gap:20px;justify-content:center}
.card{width:280px;background:#fff;padding:12px}
.card .photo{height:150px;background:linear-gradient(160deg,#d8d2c8,#b9b1a4)}
.card h3{font-size:14px;margin:10px 0 6px;color:var(--orange-dark)}
.card p{font-size:11px;line-height:1.6;color:#555}
.card .more{font-size:10px;color:var(--muted);margin-top:6px}

.news{height:410px;padding-top:40px}
.news ul{list-style:none;border-top:1px solid var(--line)}
.news li{display:flex;align-items:center;height:46px;border-bottom:1px solid var(--line);font-size:12px}
.news .date{width:110px;color:var(--muted);font-size:11px}
.news .tag{width:82px;height:20px;line-height:20px;text-align:center;color:#fff;font-size:10px;margin-right:18px}
.tag.t1{background:var(--orange)}.tag.t2{background:var(--label-blue)}.tag.t3{background:var(--label-purple)}.tag.t4{background:var(--label-green)}
.news .all{text-align:right;font-size:11px;color:var(--orange);margin-top:12px}

.pickup{height:280px}
.pickup h2{font-size:14px;border-left:4px solid var(--orange);padding-left:8px;margin-bottom:14px}
.banners{display:grid;grid-template-columns:repeat(4,1fr);gap:16px}
.banner .plate{height:58px;border:1px solid var(--line);display:flex;align-items:center;justify-content:center;gap:8px;font-size:14px;font-weight:700;color:var(--orange-dark)}
.banner .plate i{width:14px;height:14px;background:var(--orange)}
.banner p{font-size:10px;color:#555;margin-top:6px;line-height:1.5}

.other{height:300px;background:var(--dark);padding-top:34px}
.other h2{color:#fff;font-size:14px;border-left:4px solid var(--orange);padding-left:8px;margin-bottom:18px}
.other-list{display:flex;gap:12px}
.other-list div{flex:1;height:62px;background:#fff;display:flex;align-items:center;justify-content:center;font-size:14px;font-weight:700;color:var(--ink)}

.foot-nav{height:50px;background:#3b3b3b;border-top:1px solid #555;display:flex;justify-content:center;align-items:center;gap:40px;font-size:11px;color:#ddd}
.copyright{height:44px;background:#262626;color:#aaa;font-size:10px;text-align:center;line-height:44px}
</style>
</head>
<body>
<header class="site-header">
  <div class="wrap">
    <div class="brand"><small>学生会館</small>STAY-NAVI</div>
    <nav class="global-nav"><span>学生会館とは</span><span>お部屋の探し方</span><span>Q&amp;A</span><span>会社概要</span></nav>
    <span class="entry-btn">資料請求</span>
  </div>
</header>

<section class="hero">
  <div class="hero-bg" role="img" aria-label="学生が集まる明るい寮の共用スペースの写真"></div>
  <div class="hero-copy">
    <h1>学生のための安心で快適な住まい「学生会館」</h1>
    <p>ひとり暮らしを不安に感じる学生と保護者の方へ、<br>安全で快適な学生会館の情報をまとめてご紹介します。</p>
  </div>
  <div class="search-bar">
    <div class="tabs">エリア・学校名・駅名から学生会館を探す</div>
    <div class="search-row">
      <div class="select">学校名で検索</div>
      <div class="field">学校名・駅名・キーワードを入力</div>
      <div class="go"><svg width="18" height="18" viewBox="0 0 18 18"><circle cx="7.5" cy="7.5" r="5.5" fill="none" stroke="#fff" stroke-width="2"/><line x1="11.5" y1="11.5" x2="16" y2="16" stroke="#fff" stroke-width="2"/></svg></div>
    </div>
  </div>
  <div class="quick">
    <a><span class="ic"></span><em>鉄道</em>で探す</a>
    <a><span class="ic"></span><em>エリア</em>で探す</a>
    <a><span class="ic"></span><em>食事付き</em>を探す</a>
    <a><span class="ic"></span><em>学校検索</em>で探す</a>
  </div>
</section>

<div class="notice-line">全国の学生会館をエリア・学校・駅から簡単に検索できます</div>

<section class="about wrap">
  <div class="sec-title"><h2>学生会館について</h2><span>ABOUT</span></div>
  <div class="about-main">
    <a><span class="icon"></span><div><b>学生会館ってどんなところ？</b><small>学生会館の特徴やメリットをご紹介</small></div></a>
    <a><span class="icon"></span><div><b>学生会館入館の流れ</b><small>お申し込みから入館までの手順</small></div></a>
  </div>
  <div class="about-grid">
    <a><span class="icon"></span><div><b>学生会館 VS アパート</b><small>費用や設備を比較</small></div></a>
    <a><span class="icon"></span><div><b>学生会館レポート</b><small>実際の暮らしを紹介</small></div></a>
    <a><span class="icon"></span><div><b>学生会館Q&amp;A</b><small>よくある質問まとめ</small></div></a>
    <a><span class="icon"></span><div><b>学生会館の選び方</b><small>失敗しないポイント</small></div></a>
    <a><span class="icon"></span><div><b>学生会館の一日</b><small>寮生の生活をのぞく</small></div></a>
    <a><span class="icon"></span><div><b>保護者の方へ</b><small>安心のサポート体制</small></div></a>
  </div>
</section>

<section class="recommend">
  <div class="wrap">
    <div class="sec-title"><h2>おすすめの学生会館情報</h2><span>RECOMMEND</span></div>
    <div class="cards">
      <div class="card"><div class="photo" role="img" aria-label="学生会館の外観写真"></div><h3>駅前学生会館</h3><p>駅から徒歩3分、朝夕食付きで通学にも便利な学生会館です。</p><div class="more">詳しく見る ›</div></div>
      <div class="card"><div class="photo" role="img" aria-label="レンガ調の学生会館外観写真"></div><h3>緑が丘ハイツ</h3><p>閑静な住宅街にある女子専用。セキュリティも充実しています。</p><div class="more">詳しく見る ›</div></div>
      <div class="card"><div class="photo" role="img" aria-label="白い学生マンションの外観写真"></div><h3>桜坂学生館</h3><p>全室家具付き、管理人常駐で初めての一人暮らしも安心です。</p><div class="more">詳しく見る ›</div></div>
    </div>
  </div>
</section>

<section class="news wrap">
  <div class="sec-title"><h2>お知らせ/トピックス</h2><span>NEWS &amp; TOPICS</span></div>
  <ul>
    <li><span class="date">2014.02.10</span><span class="tag t1">お知らせ</span>学生会館情報掲載 ～入館をご検討の方に資料をプレゼント</li>
    <li><span class="date">2014.02.05</span><span class="tag t2">トピックス</span>一人暮らしに役立つ便利グッズをご紹介します</li>
    <li><span class="date">2014.01.28</span><span class="tag t3">新着情報</span>大手学生マンションが春の入館者を募集中です</li>
    <li><span class="date">2014.01.20</span><span class="tag t4">特集</span>女子学生向け特集ページを公開しました</li>
  </ul>
  <div class="all">一覧を見る ›</div>
</section>

<section class="pickup wrap">
  <h2>イチオシ学生会館紹介サイト</h2>
  <div class="banners">
    <div class="banner"><div class="plate"><i></i>マナビ女子寮</div><p>女子学生専用の会館情報サイト</p></div>
    <div class="banner"><div class="plate"><i></i>キャンパスハウス</div><p>首都圏の学生会館を多数掲載</p></div>
    <div class="banner"><div class="plate"><i></i>ユニ寮ガイド</div><p>食事付き会館を詳しく紹介</p></div>
    <div class="banner"><div class="plate"><i></i>ハルカ学生寮</div><p>安心の女子学生寮ガイド</p></div>
  </div>
</section>

<section class="other">
  <div class="wrap">
    <h2>学生会館以外のお部屋探し</h2>
    <div class="other-list">
      <div>ヘヤナビ</div><div>学生寮ナビ</div><div>スミカ下宿</div><div>ルームポート</div><div>寮ガイド</div>
    </div>
  </div>
</section>

<nav class="foot-nav"><span>会社概要</span><span>プライバシーポリシー</span><span>サイトマップ</span><span>お問い合わせ</span></nav>
<div class="copyright">© 学生会館STAY-NAVI All Rights Reserved.</div>
</body>
</html>
```